develop our online residential property development appraisal service

This project requires a detailed WordPress design to represent a new digital residential property development consultancy business. At its heart it will have a number of different products that essentially advise customers of the potential value and feasibility of developing their residential site into multiple townhouses, units, apartments, etc... This will be accompanied by explaining the considerations of residential property development.

We aim to navigate and break down this complex area and provide our customers with the tools, knowledge, control and power to 'unlock the value' in their property.

REFERENCE DOCUMENTS:
1. Detailed solution requirements please refer to the attached 'wordpressdesignrequirements'
2. Logo files, style guide and colour pallet please refer to the attached 'KRMV.zip'
3. Site Map refer to attached 'wordpressdesignsitemap'

Reason: Additional information provided so extending period for designs to take into account.

Target Market(s)

The site will appeal to professional service providers; accountants, financial planners, lawyers, etc…

Industry/Entity Type

Residential

Font styles to use
Sans Serif
Other font styles liked:
• Similar to the logo font, slim line and simple

Requirements
Must have
• The logo, style and colour palette provided in the attached 'KRMV.zip' files
• Satisfy the intent of the 'wordpressdesignrequirements'
• Present as an online-centric business
• Clean, crisp and modern design
• Predominant use of white as a background contrasted with the colours provided in the colour palette
Nice to have
• Use of the following WordPress business themes is encouraged but not mandatory:
• 1. Tovu
• 2. Pilmu
• 3. Vomi
Should not have
• Overt references to Australia

```html
<!DOCTYPE html>
<html lang="en">
<head>
<meta charset="utf-8">
<title>KRMV – Property Development Appraisals</title>
<link rel="stylesheet" href="https://fonts.googleapis.com/css2?family=Arimo:wght@400;700&display=swap">
<style>
:root{
  --dark:#2b2f30;
  --panel:#464646;
  --panel-bar:#3a3a3a;
  --teal:#2aa79b;
  --teal-light:#45c7b8;
  --green:#3aa86a;
  --orange:#d98a4f;
  --band:#d3e8e6;
  --text:#333;
  --muted:#8a8f90;
  --light:#c9cccd;
  --white:#fff;
}
*{box-sizing:border-box;margin:0;padding:0}
html,body{width:793px;height:1200px;overflow:hidden}
body{font-family:"Arimo",Arial,sans-serif;background:var(--white);color:var(--text);position:relative}
.abs{position:absolute}
a{color:inherit;text-decoration:none}
ul{list-style:none}

/* header */
.site-header{position:absolute;left:0;top:0;width:793px;height:83px;background:var(--dark)}
.topbar{position:absolute;left:106px;top:0;width:582px;height:23px;border-bottom:1px solid #444a4b;color:var(--light);font-size:7px}
.topbar .email{position:absolute;left:6px;top:8px;display:flex;gap:5px;align-items:center}
.topbar .login{position:absolute;left:395px;top:8px;display:flex;gap:4px;align-items:center}
.social-top{position:absolute;right:0;top:0;display:flex;height:23px}
.social-top span{width:25px;height:23px;border-left:1px solid #444a4b;display:flex;align-items:center;justify-content:center}
.social-top span i{width:6px;height:6px;background:#9ea3a4;display:block}
.brand{position:absolute;left:114px;top:39px;display:flex;align-items:center;gap:6px}
.brand .mark{width:12px;height:12px;background:var(--teal)}
.brand .name{font-size:15px;color:var(--teal);line-height:1}
.search-top{position:absolute;left:501px;top:37px;width:185px;height:18px;background:#4a4f50;color:#9ea3a4;font-size:7.5px;padding:5px 6px}
.search-top svg{position:absolute;right:6px;top:4px}
.nav{position:absolute;left:395px;top:60px;display:flex;height:23px;font-size:7px;color:var(--light)}
.nav li{padding:0 7px;line-height:23px}
.nav li.active{background:var(--teal);color:var(--white)}

/* hero */
.hero{position:absolute;left:0;top:83px;width:793px;height:219px;background:linear-gradient(180deg,#7d6c6a 0%,#b88f77 30%,#8a7a66 55%,#4c5a3c 80%,#3a4a30 100%)}
.hero-caption{position:absolute;left:106px;top:69px;width:245px;height:70px;background:rgba(30,30,30,.45);padding:10px 12px}
.hero-caption h1{font-size:13px;font-weight:400;color:var(--teal-light)}
.hero-caption p{font-size:7.5px;color:#eee;line-height:1.5;margin-top:5px}
.btn{display:inline-flex;align-items:center;gap:3px;background:var(--green);color:var(--white);font-size:7px;padding:0 6px;height:16px}
.hero .btn{position:absolute;left:107px;top:142px;height:17px}

/* about */
.section-title{font-size:13px;font-weight:400;color:var(--teal)}
.about-panel{position:absolute;left:106px;top:351px;width:379px;height:208px;background:var(--panel)}
.tabs{height:31px;background:var(--panel-bar);position:relative;font-size:7.5px;color:var(--white)}
.tabs span{position:absolute;top:12px}
.tabs .current{border-bottom:1px solid #ddd;padding-bottom:3px}
.about-photo{position:absolute;left:8px;top:44px;width:178px;height:150px;background:linear-gradient(180deg,#6fa3d8 0%,#b8cfe6 35%,#b9a58f 60%,#7f9a5c 85%,#c9c1b4 100%)}
.about-text{position:absolute;left:201px;top:41px;width:172px;font-size:7px;line-height:14.8px;color:#b8bbbc}
.about-panel .btn{position:absolute;left:205px;top:170px}
.opps li{position:absolute;left:0;width:180px;font-size:7.3px;line-height:12.5px;color:var(--muted);padding-left:11px}
.opps li svg{position:absolute;left:0;top:2px}

/* recent */
.recent{position:absolute;left:0;top:584px;width:793px;height:179px;background:var(--band)}
.recent-photo{position:absolute;left:114px;top:16px;width:275px;height:148px;background:linear-gradient(180deg,#5d9bd6 0%,#aac8e6 30%,#d8d3cc 55%,#8c7f70 78%,#6f8a55 100%)}
.recent h2{position:absolute;left:405px;top:20px}
.recent h3{position:absolute;left:405px;top:43px;font-size:10px;font-weight:400;color:#333}
.recent p{position:absolute;left:405px;top:58px;width:268px;font-size:7px;line-height:12.5px;color:var(--muted)}
.recent .btn{position:absolute;left:405px;top:141px}

/* reports */
.card{position:absolute;top:812px;width:178px}
.card .photo{height:127px}
.card .row{display:flex;justify-content:space-between;align-items:center;margin-top:5px}
.card .label{font-size:10px;color:#333;padding-left:5px}
.card .req{background:var(--orange);color:var(--white);font-size:7.5px;height:19px;line-height:19px;padding:0 6px}
.pager{position:absolute;left:381px;top:978px;display:flex;gap:4px}
.pager span{width:13px;height:12px;display:flex;align-items:center;justify-content:center}

/* footer */
.site-footer{position:absolute;left:0;top:1015px;width:793px;height:185px;background:var(--dark)}
.site-footer h4{position:absolute;font-size:10px;font-weight:400;color:var(--teal)}
.flist{position:absolute;font-size:7.5px;color:#b3b7b8}
.flist li{height:15.7px;display:flex;gap:6px;align-items:center}
.flist li b{color:var(--teal);font-weight:400}
.fsocial{position:absolute;left:120px;top:108px;display:flex;gap:7px}
.fsocial span{width:14px;height:14px;border:1px solid #858a8b;border-radius:50%}
.fsearch{position:absolute;left:504px;top:46px;width:129px;height:16px;background:#3d4243;color:#9ea3a4;font-size:6.5px;padding:4px 5px}
.fsearch svg{position:absolute;right:5px;top:3px}
.fcontact{position:absolute;left:505px;top:98px;font-size:7.5px;color:#b3b7b8;line-height:15px}
.fcontact div{display:flex;gap:4px;align-items:center}
.bottom{position:absolute;left:106px;top:157px;width:582px;border-top:1px solid #444a4b;font-size:7px;color:#ddd;padding-top:6px;padding-left:12px}
</style>
</head>
<body>

<header class="site-header">
  <div class="topbar">
    <div class="email">
      <svg width="7" height="5" viewBox="0 0 7 5"><rect width="7" height="5" fill="#9ea3a4"/><path d="M0 0l3.5 2.6L7 0" stroke="#2b2f30" fill="none" stroke-width=".8"/></svg>
      hello@krmvappraisals.example
    </div>
    <div class="login">
      <svg width="7" height="6" viewBox="0 0 7 6"><path d="M0 3h4M2.5 1.5L4 3 2.5 4.5M4.5 0.5h2v5h-2" stroke="#c9cccd" fill="none" stroke-width=".9"/></svg>
      Login / Register
    </div>
    <div class="social-top"><span><i></i></span><span><i></i></span><span><i></i></span><span><i></i></span><span><i></i></span></div>
  </div>
  <div class="brand">
    <span class="mark"></span>
    <span class="name">KRMV</span>
  </div>
  <div class="search-top">Search...
    <svg width="9" height="9" viewBox="0 0 9 9"><circle cx="3.6" cy="3.6" r="2.7" stroke="#b3b7b8" fill="none" stroke-width="1.1"/><path d="M5.6 5.6L8.5 8.5" stroke="#b3b7b8" stroke-width="1.3"/></svg>
  </div>
  <ul class="nav">
    <li class="active">Home</li><li>About Us</li><li>Property Report</li><li>Property Development</li><li>Contact Us</li>
  </ul>
</header>

<section class="hero" role="img" aria-label="Modern two-storey white house with glowing windows at dusk">
  <div class="hero-caption">
    <h1>Necessitatibus Saepe Eveniet</h1>
    <p>At vero eos et accusamus et iusto odio dignissimos ducimus qui blanditiis praesentium voluptatum...</p>
  </div>
  <a class="btn" href="#">Know More &raquo;</a>
</section>

<h2 class="section-title abs" style="left:118px;top:324px">Know About US</h2>
<div class="about-panel">
  <div class="tabs">
    <svg class="abs" style="left:0;top:0" width="379" height="31" viewBox="0 0 379 31"><path d="M143 2L133 29M232 2L222 29" stroke="#888" stroke-width="1"/></svg>
    <span class="current" style="left:74px">WHO are we?</span>
    <span style="left:148px">WHAT do we do?</span>
    <span style="left:237px">HOW do we do it?</span>
  </div>
  <div class="about-photo" role="img" aria-label="Two-storey family home with landscaped front garden"></div>
  <p class="about-text">KRMV Property Development Appraisals is a digital residential property development consultancy business. At its heart it will have a number of different products that essentially advise customers of the potential value and feasibility of developing their residential site into multiple townhouses, units, apartments, etc...</p>
  <a class="btn" href="#">Know More &raquo;</a>
</div>

<h2 class="section-title abs" style="left:506px;top:324px">Opportunities</h2>
<ul class="opps abs" style="left:506px;top:350px">
  <li style="top:0"><svg width="7" height="7" viewBox="0 0 7 7"><path d="M3.5 0L7 3.2H6V7H1V3.2H0z" fill="var(--green)"/></svg>Sed quia non numquam eius dolor sit amet, consectetur.</li>
  <li style="top:35.5px"><svg width="7" height="7" viewBox="0 0 7 7"><path d="M3.5 0L7 3.2H6V7H1V3.2H0z" fill="var(--green)"/></svg>Labore et dolore laboris nisi ut aliquip ex ea commodo consequat.</li>
  <li style="top:71px"><svg width="7" height="7" viewBox="0 0 7 7"><path d="M3.5 0L7 3.2H6V7H1V3.2H0z" fill="var(--green)"/></svg>Corporis suscipit laboriosa messe cillum dolore eu fugiat nulla.</li>
  <li style="top:106.5px"><svg width="7" height="7" viewBox="0 0 7 7"><path d="M3.5 0L7 3.2H6V7H1V3.2H0z" fill="var(--green)"/></svg>Similique sunt in culpa et quasi architecto beatae vitae dicta sunt explicabo.</li>
  <li style="top:142px"><svg width="7" height="7" viewBox="0 0 7 7"><path d="M3.5 0L7 3.2H6V7H1V3.2H0z" fill="var(--green)"/></svg>Quod maxime plac consequuntur magni dolores eos qui ratione.</li>
  <li style="top:177.5px"><svg width="7" height="7" viewBox="0 0 7 7"><path d="M3.5 0L7 3.2H6V7H1V3.2H0z" fill="var(--green)"/></svg>Ta sunt explicabo nemo enim ipsam volu ptatem quia voluptas sitqui.</li>
</ul>

<section class="recent">
  <div class="recent-photo" role="img" aria-label="Contemporary rendered house with stone feature wall"></div>
  <h2 class="section-title">Recent Property Development</h2>
  <h3>Soluta Nobis Est</h3>
  <p>Temporibus autem quibusdam et aut officiis debitis aut rerum necess tatibus saepe eveniet.Neque porro quisquam est, qui dolorem ipsum quia dolor sit amet, consectetur, adipisci velit, sedm nisi ut aliquid ex ea commodi consequatur? Quis autem vel eum iure reprehenderit qui in ea voluptate velit esse quam nihil molestiae consequatur, vel illum qui dolorem eum fugiat quo voluptas nulla pariatur...</p>
  <a class="btn" href="#">Know More &raquo;</a>
</section>

<h2 class="section-title abs" style="left:118px;top:786px">Property Report Summary</h2>
<div class="card" style="left:114px">
  <div class="photo" role="img" aria-label="Heritage weatherboard house with cottage garden" style="background:linear-gradient(180deg,#8fb6de 0%,#c9d6d2 35%,#8e8a7a 60%,#5f8a3c 85%,#7a9a4c 100%)"></div>
  <div class="row"><span class="label">Property Report A</span><span class="req">Request Report</span></div>
</div>
<div class="card" style="left:308px">
  <div class="photo" role="img" aria-label="Modern two-storey house with garage" style="background:linear-gradient(180deg,#6fa6d9 0%,#c2d3e2 30%,#d9d7d0 55%,#8a7b68 80%,#5f7f48 100%)"></div>
  <div class="row"><span class="label">Property Report B</span><span class="req">Request Report</span></div>
</div>
<div class="card" style="left:501px">
  <div class="photo" role="img" aria-label="Timber-clad contemporary home with balcony" style="background:linear-gradient(180deg,#4f8fd0 0%,#a9c6e4 30%,#c9b39a 55%,#8a6a52 80%,#6b7a5a 100%)"></div>
  <div class="row"><span class="label">Property Report C</span><span class="req">Request Report</span></div>
</div>
<div class="pager">
  <span style="background:var(--green)"><svg width="5" height="6" viewBox="0 0 5 6"><path d="M5 0v6L0 3z" fill="#fff"/></svg></span>
  <span style="background:#dcdcdc"><svg width="5" height="6" viewBox="0 0 5 6"><path d="M0 0v6l5-3z" fill="#fff"/></svg></span>
</div>

<footer class="site-footer">
  <h4 style="left:119px;top:31px">About Us</h4>
  <ul class="flist" style="left:119px;top:43px">
    <li><b>&rsaquo;</b>WHO we are?</li><li><b>&rsaquo;</b>WHAT do we do?</li><li><b>&rsaquo;</b>HOW do we do it?</li>
  </ul>
  <div class="fsocial"><span></span><span></span><span></span><span></span><span></span></div>

  <h4 style="left:311px;top:31px">Links</h4>
  <ul class="flist" style="left:308px;top:43px">
    <li><b>&rsaquo;</b>About US</li><li><b>&rsaquo;</b>Opportunities</li><li><b>&rsaquo;</b>Property Report</li><li><b>&rsaquo;</b>Property Development</li><li><b>&rsaquo;</b>Contact Us</li><li><b>&rsaquo;</b>Site Map</li>
  </ul>

  <h4 style="left:505px;top:31px">Search</h4>
  <div class="fsearch">Enter your email ...
    <svg width="9" height="9" viewBox="0 0 9 9"><circle cx="3.6" cy="3.6" r="2.7" stroke="#b3b7b8" fill="none" stroke-width="1.1"/><path d="M5.6 5.6L8.5 8.5" stroke="#b3b7b8" stroke-width="1.3"/></svg>
  </div>
  <h4 style="left:505px;top:81px">Contact &nbsp;Us</h4>
  <div class="fcontact">
    <div><svg width="6" height="5" viewBox="0 0 7 5"><rect width="7" height="5" fill="#9ea3a4"/></svg>hello@krmvappraisals.example</div>
    <div><svg width="6" height="6" viewBox="0 0 6 6"><path d="M1 0h1.5l.6 1.6-.9.7a4 4 0 0 0 1.5 1.5l.7-.9L6 3.5V5c0 .6-.5 1-1 1A5 5 0 0 1 0 1c0-.5.4-1 1-1z" fill="#9ea3a4"/></svg>0-000-000-0000</div>
  </div>
  <div class="bottom">&copy; Copyright information here</div>
</footer>

</body>
</html>
```